Graphic design for an existing cardboard Archive box

We need a graphic design for an existing archive box packaging.
Our request is really simple: we would like to have a graphic design that is pleasant to put in the office or on the bookshelf in the living room.
The project must be in CMYK color space, no other colors (Pantone, spot colors, metallic inks, ecc) or varnishes can be used.
You can see and download some sample pictures and the complete flat template in Adobe Illustrator, EPS, and PDF file.

Target Market(s)

Both individual customers and professional

Industry/Entity Type

Graphic Design

Requirements
Must have
• REALLY IMPORTANT: we'd like to see 2 files: "flat graphic" on the template and applied on the 3D. Thank you

Graphic design that is pleasant to put in the office or on the bookshelf in the living room.

CMYK color space only.

We like colorful images, positive and tempting graphics.

```html
<!DOCTYPE html>
<html lang="en">
<head>
<meta charset="utf-8">
<title>Archive Box – Flat Graphic</title>
<link href="https://fonts.googleapis.com/css2?family=Open+Sans:wght@400;700&display=swap" rel="stylesheet">
<style>
  :root {
    --bg: #e4e7ea;
    --board: #ffffff;
    --fold: #c9ccd0;
    --ink: #3d4a5c;
    --lime: #8cc63f;
    --magenta: #d6246e;
    --cyan: #1fb3d6;
    --purple: #6b3fa0;
    --orange: #f08a1c;
  }
  html, body {
    margin: 0;
    width: 1200px;
    height: 1200px;
    overflow: hidden;
    background: var(--bg);
    font-family: "Open Sans", Arial, sans-serif;
  }
  .canvas { position: relative; width: 1200px; height: 1200px; }

  .panel {
    position: absolute;
    background: var(--board);
    border: 1px solid var(--fold);
    box-sizing: border-box;
    overflow: hidden;
  }
  .back   { left: 150px; top: 320px; width: 380px; height: 560px; }
  .spine  { left: 530px; top: 320px; width: 140px; height: 560px; }
  .front  { left: 670px; top: 320px; width: 380px; height: 560px; }
  .flap-top    { left: 530px; top: 200px; width: 140px; height: 120px; border-radius: 18px 18px 0 0; }
  .flap-bottom { left: 530px; top: 880px; width: 140px; height: 120px; border-radius: 0 0 18px 18px; }

  /* diagonal stream of colour where the tumbling puzzle pieces belong */
  .puzzle-stream {
    position: absolute;
    inset: 0;
    background:
      radial-gradient(circle at 78% 10%, rgba(107,63,160,.85) 0 5%, transparent 10%),
      radial-gradient(circle at 92% 6%,  rgba(140,198,63,.8) 0 4%, transparent 8%),
      radial-gradient(circle at 58% 24%, rgba(214,36,110,.85) 0 5%, transparent 10%),
      radial-gradient(circle at 80% 30%, rgba(140,198,63,.85) 0 6%, transparent 11%),
      radial-gradient(circle at 22% 42%, rgba(240,138,28,.85) 0 5%, transparent 10%),
      radial-gradient(circle at 62% 46%, rgba(31,179,214,.85) 0 6%, transparent 11%),
      radial-gradient(circle at 36% 54%, rgba(214,36,110,.8) 0 4%, transparent 8%),
      radial-gradient(circle at 14% 62%, rgba(31,179,214,.8) 0 4%, transparent 8%),
      radial-gradient(circle at 46% 64%, rgba(107,63,160,.8) 0 5%, transparent 9%),
      radial-gradient(circle at 18% 78%, rgba(214,36,110,.9) 0 8%, transparent 14%),
      linear-gradient(215deg, rgba(140,198,63,.25), rgba(31,179,214,.25) 35%, rgba(107,63,160,.22) 60%, rgba(214,36,110,.22));
    clip-path: polygon(55% 0, 100% 0, 100% 22%, 40% 95%, 0 95%, 0 45%);
  }
  .front .puzzle-stream {
    clip-path: polygon(30% 0, 100% 0, 100% 30%, 70% 100%, 20% 100%, 40% 45%);
  }
  .spine .spine-piece {
    position: absolute; left: 60px; top: 470px; width: 60px; height: 60px;
    border-radius: 10px;
    background: radial-gradient(circle at 40% 40%, #5fd0ea, var(--cyan));
  }

  .swoosh {
    position: absolute;
    left: 0; right: 0; bottom: 0; height: 150px;
    background: linear-gradient(100deg,
      rgba(214,36,110,.18), rgba(240,138,28,.18) 30%,
      rgba(140,198,63,.18) 55%, rgba(31,179,214,.22) 80%, rgba(107,63,160,.15));
  }

  .logo-slot {
    position: absolute;
    left: 70px; top: 420px;
    transform: rotate(-90deg);
    transform-origin: left top;
    display: flex; align-items: center; gap: 12px;
    color: var(--ink);
    white-space: nowrap;
  }
  .logo-slot .rule { width: 2px; height: 44px; background: var(--lime); }
  .logo-slot .lead { font-size: 20px; font-weight: 400; line-height: 1.1; }
  .logo-slot .name { font-size: 26px; font-weight: 700; letter-spacing: 1px; line-height: 1.1; }

  .spine-label {
    position: absolute; left: 20px; top: 24px;
    width: 100px; height: 250px;
    border: 1px solid var(--fold);
    box-sizing: border-box;
  }
  .spine-label .caption {
    position: absolute; left: 8px; top: 10px;
    font-size: 16px; color: var(--ink); line-height: 1.05;
  }
  .spine-label .line {
    position: absolute; left: 8px; right: 8px; height: 1px; background: var(--fold);
  }
  .thumb-hole {
    position: absolute; left: 50%; top: 330px;
    width: 48px; height: 48px; margin-left: -24px;
    border-radius: 50%;
    border: 1px solid var(--fold);
    background: var(--bg);
  }
</style>
</head>
<body>
<main class="canvas">
  <section class="panel flap-top"></section>

  <section class="panel back">
    <div class="swoosh"></div>
    <div class="puzzle-stream" role="img" aria-label="Colourful 3D puzzle pieces tumbling diagonally across a faint grey puzzle pattern"></div>
  </section>

  <section class="panel spine">
    <div class="spine-label">
      <div class="caption">logo<br>area</div>
      <div class="line" style="top:80px"></div>
      <div class="line" style="top:110px"></div>
      <div class="line" style="top:140px"></div>
      <div class="line" style="top:170px"></div>
      <div class="line" style="top:200px"></div>
      <div class="line" style="top:230px"></div>
    </div>
    <div class="thumb-hole"></div>
    <div class="spine-piece" role="img" aria-label="A cyan puzzle piece near the base of the spine"></div>
  </section>

  <section class="panel front">
    <div class="swoosh"></div>
    <div class="puzzle-stream" role="img" aria-label="Colourful 3D puzzle pieces streaming down the cover"></div>
    <div class="logo-slot">
      <span class="rule"></span>
      <div>
        <div class="lead">put your</div>
        <div class="name">LOGO AREA</div>
      </div>
    </div>
  </section>

  <section class="panel flap-bottom"></section>
</main>
</body>
</html>
```